Modern Business Card For A Digital Advertising Company

I'll be print on the Tarn Prints Velour paper http://us.tarnprints.example/products/velour/business-cards.html
Need's to be modern and use the color palette of the logo or gray scales. I think integrating the pixelation of the logo in to the card and having it wrap from one side to the other could be interesting. My company provides ad operations, web development, and number of other services to websites around the world. You can see my website at http://www.pixelharbor.example
Contact info on the card needs to have
Dana Welloby
President
p.555.318.4406
dana@pixelharbor.example
http://www.pixelharbor.example
Doesn't necessarily need to be in that order
Target Market(s)
Website owners
Industry/Entity Type
Business
Look and feel

```html
<!DOCTYPE html>
<html lang="en">
<head>
<meta charset="utf-8">
<title>Pixel Harbor — Business Card</title>
<link rel="stylesheet" href="https://fonts.googleapis.com/css2?family=Source+Sans+3:wght@400;600&display=swap">
<style>
  :root {
    --bg: #e4e2dd;
    --card: #eef0ec;
    --band: #6a6b6d;
    --band-light: #8c8d8f;
    --info: #9c9d9f;
    --green: #8cc63f;
    --green-soft: #a8d66a;
    --white: #ffffff;
    --shadow: rgba(0,0,0,0.28);
  }
  * { box-sizing: border-box; margin: 0; padding: 0; }
  html, body { width: 1200px; height: 1000px; overflow: hidden; }
  body {
    background: var(--bg);
    font-family: "Source Sans 3", "Segoe UI", sans-serif;
    position: relative;
  }
  .card {
    position: absolute;
    width: 620px;
    height: 370px;
    background: var(--card);
    box-shadow: 6px 10px 22px var(--shadow);
    overflow: hidden;
  }
  .card--front { left: 132px; top: 100px; }
  .card--back  { left: 350px; top: 540px; }

  .band {
    position: absolute;
    background: var(--band);
    box-shadow: 0 8px 14px rgba(0,0,0,0.3);
  }
  .card--front .band { left: 0; top: 76px; width: 520px; height: 230px; }
  .card--front .band-edge {
    position: absolute; left: 0; top: 76px; width: 505px; height: 230px;
    background: var(--band-light); opacity: .35; transform: translate(8px,-6px);
  }

  .pixel-strip {
    position: absolute;
    background: linear-gradient(90deg, var(--green), var(--green-soft));
  }
  .card--front .pixel-strip { left: 0; top: 96px; width: 138px; height: 52px; }

  .wordmark {
    position: absolute;
    left: 200px; top: 160px;
    display: flex; align-items: center; gap: 14px;
  }
  .wordmark__mark { width: 34px; height: 34px; background: var(--green); }
  .wordmark__name {
    font-size: 40px; font-weight: 600; color: var(--green);
    letter-spacing: .5px;
  }

  .card--back .band { left: 0; top: 110px; width: 560px; height: 215px; }
  .card--back .pixel-strip--band { left: 0; top: 120px; width: 520px; height: 52px; }
  .card--back .pixel-strip--tail { left: 520px; top: 100px; width: 100px; height: 52px; }

  .stripe-field {
    position: absolute; left: 180px; top: 275px; width: 320px; height: 95px;
    background: linear-gradient(135deg, var(--green), var(--green-soft));
  }

  .contact {
    position: absolute; left: 20px; top: 220px; width: 310px; height: 120px;
    background: var(--info);
    box-shadow: 0 8px 14px rgba(0,0,0,0.3);
    padding: 24px 0 0 30px;
    color: var(--white);
  }
  .contact__row { display: flex; align-items: baseline; height: 20px; }
  .contact__label { width: 58px; font-size: 12px; }
  .contact__value { font-size: 16px; }

  .identity {
    position: absolute; right: 80px; top: 182px; text-align: right;
    color: var(--white);
  }
  .identity__name { font-size: 34px; line-height: 1; }
  .identity__title { font-size: 15px; margin-right: 40px; }
</style>
</head>
<body>

<section class="card card--front" aria-label="Card front">
  <div class="band-edge"></div>
  <div class="band"></div>
  <div class="pixel-strip" role="img" aria-label="Green pixel grid strip"></div>
  <div class="wordmark">
    <span class="wordmark__mark"></span>
    <span class="wordmark__name">Pixel Harbor</span>
  </div>
</section>

<section class="card card--back" aria-label="Card back">
  <div class="band"></div>
  <div class="pixel-strip pixel-strip--band" role="img" aria-label="Green pixel grid strip"></div>
  <div class="pixel-strip pixel-strip--tail" role="img" aria-label="Green pixel grid continuing past the band"></div>
  <div class="stripe-field" role="img" aria-label="Green diagonal stripe block"></div>
  <div class="identity">
    <p class="identity__name">Dana Welloby</p>
    <p class="identity__title">President</p>
  </div>
  <div class="contact">
    <p class="contact__row"><span class="contact__label">Phone:</span><span class="contact__value">555.318.4406</span></p>
    <p class="contact__row"><span class="contact__label">Web:</span><span class="contact__value">www.pixelharbor.example</span></p>
    <p class="contact__row"><span class="contact__label">Email:</span><span class="contact__value">dana@pixelharbor.example</span></p>
  </div>
</section>

</body>
</html>
```